Birch Endodontics business stationary
stationary, envelopes, business cards, referral pad, digital signature for email
Professional
R. Marlowe Birch, DDS, MS
2267 Orchard Crest Dr
Monroe, NC 28471
toothcare@birchendo-example.com
www.birchendo-example.com
I'm going to upload a couple of sample referral pads from other endodontic offices. Please refer to these for a template. I will also upload a couple of maps. I need a simple map drawn to find the office. Voxmap address is wrong. I will mark the location on the map I upload. The fax number I listed will be changed in a couple days so I will update with the correct number.
I need the back to be a place where the patient's appointment date and time can be recorded.
This is the logo to be used.
Please reference these to draw a simple map on the back of the referral pad
map
sample referral pad
I like the style of this pad alot.
I like this referral pad
I sketched how the map should look.
I sketched the layout for the referral pad.

```html
<!DOCTYPE html>
<html lang="en">
<head>
<meta charset="utf-8">
<title>Birch Endodontics Stationery</title>
<link href="https://fonts.googleapis.com/css2?family=Open+Sans:wght@400;600;700&display=swap" rel="stylesheet">
<style>
:root{
  --bg:#ececec;
  --paper:#ffffff;
  --blue:#1f8fcf;
  --green:#8cc43f;
  --ink:#3a3a3a;
  --muted:#7a7a7a;
}
*{box-sizing:border-box;margin:0;padding:0}
html,body{width:1200px;height:897px;overflow:hidden;background:var(--bg);font-family:"Open Sans",Arial,sans-serif;color:var(--ink)}
.canvas{position:relative;width:1200px;height:897px}
.sheet,.card{position:absolute;background:var(--paper);box-shadow:0 3px 10px rgba(0,0,0,.18);overflow:hidden}
.top-band{position:absolute;left:0;right:0;top:0;height:8px;background:var(--blue);border-bottom:3px solid var(--green)}
.brand{display:flex;align-items:center;gap:6px;color:var(--blue);font-weight:700;line-height:1;white-space:nowrap}
.brand-dot{width:18px;height:18px;border-radius:50%;background:var(--green);flex:none}
.brand-name{font-size:20px;letter-spacing:-.3px}

/* letterhead */
.letterhead{left:160px;top:162px;width:482px;height:644px}
.letterhead .brand{position:absolute;left:34px;top:34px}
.letter-body{position:absolute;left:34px;top:150px;width:420px;font-size:6.6px;line-height:1.6;color:var(--muted)}
.letter-body p{margin-bottom:8px}
.letter-body .recipient{margin-bottom:12px}
.letter-body .closing{margin-top:16px}
.letter-footer{position:absolute;left:34px;right:20px;bottom:14px;font-size:6.4px;color:var(--ink);white-space:nowrap}
.letter-footer .sep{color:var(--blue)}

/* business card */
.biz-card{left:678px;top:189px;width:404px;height:254px;border-radius:12px}
.biz-card .brand{position:absolute;left:40px;top:40px}
.biz-contact{position:absolute;left:31px;top:148px;font-size:8.5px;line-height:1.45;color:var(--ink)}
.biz-contact b{color:var(--blue);font-weight:600}
.biz-name{position:absolute;right:36px;top:170px;font-size:14px;font-weight:700;color:var(--blue);white-space:nowrap}

/* appointment card */
.appt-card{left:678px;top:460px;width:404px;height:237px;border-radius:12px}
.appt-card .brand{position:absolute;left:50%;top:26px;transform:translateX(-50%)}
.appt-title{position:absolute;left:0;right:0;top:76px;text-align:center;font-size:9px;font-weight:600}
.appt-fields{position:absolute;left:77px;right:62px;top:128px;display:flex;gap:10px;font-size:8.5px}
.appt-fields .field{display:flex;align-items:flex-end;gap:4px;flex:1}
.appt-fields .line{flex:1;border-bottom:1px solid var(--ink);height:9px}
.appt-days{position:absolute;left:78px;right:62px;top:154px;display:flex;justify-content:space-between}
.day{display:flex;flex-direction:column;align-items:center;gap:5px;font-size:7.5px}
.day .box{width:24px;height:17px;border:1px solid var(--ink)}
</style>
</head>
<body>
<div class="canvas">

  <section class="sheet letterhead">
    <div class="top-band"></div>
    <div class="brand"><span class="brand-dot"></span><span class="brand-name">birch endodontics</span></div>
    <div class="letter-body">
      <p class="recipient">Referring Doctor<br>100 Main Street<br>Charlotte, NC</p>
      <p>Dear Doctor Colleague,</p>
      <p>Thank you for referring your patient to our office. We completed a full evaluation today, including digital radiographs and pulp testing of the affected tooth. Our findings confirmed irreversible pulpitis, and we recommended root canal therapy to preserve the natural tooth and relieve discomfort.</p>
      <p>Treatment was completed in a single visit under local anesthesia. The patient tolerated the procedure well and left our office comfortable. A temporary restoration was placed, and we advise a permanent crown within the next few weeks.</p>
      <p>Post-operative radiographs are enclosed for your records. We will schedule a recall examination in six months to confirm healing of the periapical tissues and will share the results with your office.</p>
      <p>Please do not hesitate to call us with any questions. We appreciate your trust and look forward to working with you again.</p>
      <p class="closing">Best regards,<br>R. Marlowe Birch</p>
    </div>
    <div class="letter-footer">2267 Orchard Crest Dr, Monroe, NC 28471 <span class="sep">|</span> P: 704-555-0142 <span class="sep">|</span> F: 704-555-0187 <span class="sep">|</span> toothcare@birchendo-example.com</div>
  </section>

  <section class="card biz-card">
    <div class="top-band"></div>
    <div class="brand"><span class="brand-dot"></span><span class="brand-name">birch endodontics</span></div>
    <div class="biz-contact">
      2267 Orchard Crest Dr<br>
      Monroe, NC 28471<br>
      <b>P:</b> 704-555-0142<br>
      <b>F:</b> 704-555-0187<br>
      <b>E:</b> toothcare@birchendo-example.com
    </div>
    <div class="biz-name">R. Marlowe Birch, DDS, MS</div>
  </section>

  <section class="card appt-card">
    <div class="brand"><span class="brand-dot"></span><span class="brand-name">birch endodontics</span></div>
    <div class="appt-title">My Next Appointment</div>
    <div class="appt-fields">
      <div class="field"><span>Date:</span><span class="line"></span></div>
      <div class="field"><span>Time/Hours:</span><span class="line"></span></div>
    </div>
    <div class="appt-days">
      <div class="day"><span>Mon</span><span class="box"></span></div>
      <div class="day"><span>Tues</span><span class="box"></span></div>
      <div class="day"><span>Wed</span><span class="box"></span></div>
      <div class="day"><span>Thu</span><span class="box"></span></div>
      <div class="day"><span>Fri</span><span class="box"></span></div>
    </div>
  </section>

</div>
</body>
</html>
```